Corporate Design für Austausch & Neuerrichtung von Heizungs- und Klimatechnik
Zielgruppe
Austausch, Neuerrichtung modernster Heizungstechnik und Klimatechnik
Unsere Zielgruppe sind Privatpersonen die Ihr Haus zukunftsorientiert beheizen bzw. kühlen wollen
Aufgabenstellung
schlicht, modern, klar
gerne schwarzer Hintergrund und max 3 Farben gerne auch kräftig / auffällig
Nur eine Idee: Vielleicht können kleine Icons im Logo erscheinen.... z.b. 4 Elemente.... Feuer, Wasser, Luft, Erde plus schneeflocke für die klimatechnik (?)

```html
<!DOCTYPE html>
<html lang="de">
<head>
<meta charset="utf-8">
<title>Thermora – Briefumschlag</title>
<link rel="stylesheet" href="https://fonts.googleapis.com/css2?family=Nunito+Sans:wght@400;600&display=swap">
<style>
  :root {
    --stage: #4d4d4d;
    --paper: #ffffff;
    --flap: #383838;
    --brand-blue: #2a4fa0;
    --accent-blue: #1ba0e2;
    --band: #79b1c8;
    --text-grey: #7a7a7a;
    --url-grey: #6e6e6e;
    --faint: #eaf4fb;
  }
  * { margin: 0; padding: 0; box-sizing: border-box; }
  html, body {
    width: 1200px; height: 1200px; overflow: hidden;
    background: var(--stage);
    font-family: "Nunito Sans", Arial, sans-serif;
  }
  .canvas { position: relative; width: 1200px; height: 1200px; }

  .envelope {
    position: absolute; left: 309px; width: 557px; height: 280px;
    background: var(--paper); overflow: hidden;
  }
  .envelope--back { top: 202px; }
  .envelope--front { top: 600px; }

  .flap { position: absolute; left: 0; top: 0; width: 557px; height: 80px; }
  .flap-mark {
    position: absolute; left: 269px; top: 21px; width: 20px; height: 20px;
    border-radius: 50%; background: var(--accent-blue);
  }

  .sender { position: absolute; left: 41px; top: 38px; }
  .sender-name {
    display: flex; align-items: center; gap: 12px;
    font-size: 33px; font-weight: 600; color: var(--brand-blue);
    line-height: 1; letter-spacing: -0.2px;
  }
  .sender-dot {
    width: 44px; height: 44px; border-radius: 50%; background: var(--accent-blue);
  }
  .sender-tagline {
    margin: -8px 0 0 56px; font-size: 9.5px; color: var(--text-grey);
    letter-spacing: 0.2px;
  }
  .sender-tagline .divider { color: var(--accent-blue); }
  .sender-address {
    margin-top: 12px; font-size: 8px; color: var(--text-grey);
    letter-spacing: 0.4px;
  }
  .sender-address .sep { margin: 0 6px; }

  .watermark {
    position: absolute; left: 440px; top: 118px; width: 110px; height: 110px;
    border-radius: 50%; background: var(--faint);
  }

  .footer-band {
    position: absolute; left: 0; top: 246px; width: 100%; height: 7px;
    background: var(--band);
  }
  .footer-url {
    position: absolute; left: 0; top: 255px; width: 100%;
    text-align: center; font-size: 12.5px; color: var(--url-grey);
  }
</style>
</head>
<body>
<main class="canvas">
  <section class="envelope envelope--back" aria-label="Umschlag Rückseite">
    <svg class="flap" viewBox="0 0 557 80" aria-hidden="true">
      <path d="M0 0 H557 L532 68 Q527 79 512 79 H45 Q30 79 25 68 Z" fill="var(--flap)"/>
    </svg>
    <span class="flap-mark" aria-hidden="true"></span>
  </section>

  <section class="envelope envelope--front" aria-label="Umschlag Vorderseite">
    <div class="sender">
      <div class="sender-name"><span class="sender-dot" aria-hidden="true"></span>Thermora</div>
      <p class="sender-tagline">effizient <span class="divider">|</span> nachhaltig <span class="divider">|</span> persönlich</p>
      <p class="sender-address">Am Mühlgraben 2<span class="sep">•</span>36100 Talbach an der Aue</p>
    </div>
    <span class="watermark" aria-hidden="true"></span>
    <div class="footer-band"></div>
    <p class="footer-url">www.thermora-haustechnik.de</p>
  </section>
</main>
</body>
</html>
```